Party Favors and Decorations Business Needs A Business Card Design

We are in need of a Logo design and business card design for a new small business called Lark Meadow Designs. We create party decorations and favours for Bridal Showers, Baby Showers, Weddings Birthdays etc. This is a very personalized service based on Clients theme, colour, and style. We are looking for a high end elegant look. I have attached a file to the style I like including the type of paper.

Target Market(s)

women, young adults, expectant mothers, mothers

Industry/Entity Type

Small Business

Contact Information for Business Card

Lark Meadow Designs Essex, ON 519-608-1942 larkmeadowdesigns.ca dana@larkmeadowgiftwrapping.com find us on Friendlink

Logo Text

Lark Meadow Designs

Font styles to use
Script

Requirements
Must have
• Name, email, web address, phone number
Should not have
• cutesy graphics

```html
<!DOCTYPE html>
<html lang="en">
<head>
<meta charset="utf-8">
<title>Lark Meadow Designs – Business Card</title>
<link rel="stylesheet" href="https://fonts.googleapis.com/css2?family=Pinyon+Script&family=Marcellus&display=swap">
<style>
  :root {
    --page: #ffffff;
    --card: #ebebeb;
    --ink: #111111;
    --frame: #4a4a4a;
    --ornament: #5a5a5a;
  }
  * { margin: 0; padding: 0; box-sizing: border-box; }
  html, body {
    width: 1200px;
    height: 900px;
    overflow: hidden;
    background: var(--page);
  }
  .canvas {
    position: relative;
    width: 1200px;
    height: 900px;
  }
  .card {
    position: absolute;
    left: 243px;
    width: 704px;
    height: 391px;
    background: var(--card);
  }
  .card--front { top: 29px; }
  .card--back { top: 477px; }
  .card__frame {
    position: absolute;
    inset: 0;
    width: 704px;
    height: 391px;
  }
  .frame-line {
    fill: none;
    stroke: var(--frame);
    stroke-width: 1.3;
  }
  .brand-name {
    position: absolute;
    font-family: "Pinyon Script", cursive;
    font-weight: 400;
    color: var(--ink);
    white-space: nowrap;
    line-height: 1;
  }
  .card--front .brand-name {
    left: 0;
    right: 0;
    top: 46px;
    text-align: center;
    font-size: 56px;
  }
  .card--back .brand-name {
    left: 355px;
    top: 195px;
    font-size: 70px;
    transform: translate(-50%, -50%) rotate(-24deg);
  }
  .contact {
    position: absolute;
    left: 0;
    right: 0;
    text-align: center;
    font-family: "Marcellus", serif;
    color: var(--ink);
    font-size: 20px;
    line-height: 1;
    white-space: nowrap;
  }
  .contact--email { top: 146px; }
  .contact--phone { top: 267px; }
  .contact--web { top: 300px; }
  .divider-ornament {
    position: absolute;
    left: 324px;
    top: 201px;
    width: 58px;
    height: 16px;
    border-radius: 8px;
    background: var(--ornament);
  }
</style>
</head>
<body>
<main class="canvas">

  <section class="card card--front" aria-label="Business card front">
    <svg class="card__frame" viewBox="0 0 704 391" aria-hidden="true">
      <rect class="frame-line" x="20" y="12" width="664" height="367"/>
      <path class="frame-line" d="M20 209 H310 M398 209 H684"/>
    </svg>
    <h1 class="brand-name">Lark Meadow Designs</h1>
    <p class="contact contact--email">dana@larkmeadowgiftwrapping.com</p>
    <div class="divider-ornament" role="img" aria-label="Small scroll flourish ornament in the centre of the divider"></div>
    <p class="contact contact--phone">Phone No: 519-608-1942</p>
    <p class="contact contact--web">Website: larkmeadowdesigns.ca</p>
  </section>

  <section class="card card--back" aria-label="Business card back">
    <svg class="card__frame" viewBox="0 0 704 391" aria-hidden="true">
      <rect class="frame-line" x="20" y="12" width="664" height="367"/>
    </svg>
    <p class="brand-name">Lark Meadow Designs</p>
  </section>

</main>
</body>
</html>
```